Business Cards & Stationary for Solo Attorney
Marcus Tolland Counsellor At Law
Business Cards & Stationary for Solo Attorney - Law
Creative Brief
Professional
Marcus Tolland
Counsellor At Law
482 Brindlecombe Avenue, 5th Floor Ashgrove, Northvale 08347
mtollandlaw@quillpost.example
tollandlawfirm.example

```html
<!DOCTYPE html>
<html lang="en">
<head>
<meta charset="utf-8">
<title>Marcus Tolland Counsellor At Law – Business Cards</title>
<link href="https://fonts.googleapis.com/css2?family=Cinzel:wght@400;600&family=Open+Sans:wght@400;600&display=swap" rel="stylesheet">
<style>
  :root {
    --navy: #1f2b5e;
    --paper: #ffffff;
    --ink: #3a3a3a;
    --rule: #9aa0b4;
    --backdrop: #d9d4cc;
    --label-ink: #5b554d;
  }
  * { box-sizing: border-box; margin: 0; padding: 0; }
  html, body { width: 1200px; height: 787px; overflow: hidden; }
  body { background: var(--backdrop); font-family: "Open Sans", Arial, sans-serif; position: relative; }

  .sheet-label {
    position: absolute; width: 535px; text-align: center;
    font-size: 19px; color: var(--label-ink);
  }
  .card {
    position: absolute; width: 535px; height: 320px; border-radius: 16px;
    background: var(--paper); overflow: hidden;
    box-shadow: 0 6px 14px rgba(0,0,0,.22);
  }
  .card--dark { background: var(--navy); color: var(--paper); }

  .mark { position: absolute; left: 0; right: 0; display: flex; align-items: center; justify-content: center; gap: 10px; color: var(--navy); }
  .card--dark .mark { color: var(--paper); }
  .mark__dot { border-radius: 50%; border: 2px solid currentColor; }
  .mark__name { font-family: "Cinzel", Georgia, serif; font-weight: 600; letter-spacing: 2px; }

  .wordmark { position: absolute; left: 0; right: 0; text-align: center; font-family: "Cinzel", Georgia, serif; color: var(--navy); }
  .card--dark .wordmark { color: var(--paper); }
  .wordmark__name { font-size: 34px; line-height: 1; letter-spacing: 1px; }
  .wordmark__title {
    display: flex; align-items: center; justify-content: center; gap: 8px;
    font-size: 13px; letter-spacing: 1.5px; margin-top: 6px;
  }
  .wordmark__title::before, .wordmark__title::after {
    content: ""; width: 34px; height: 1px; background: currentColor;
  }
  .site {
    position: absolute; left: 0; right: 0; text-align: center;
    font-family: "Cinzel", Georgia, serif; font-size: 16px; letter-spacing: 3px; color: #333;
  }
  .card--dark .site { color: var(--paper); }

  .front .wordmark__name { font-size: 30px; }
  .band {
    position: absolute; top: 178px; left: 0; right: 0; height: 66px;
    background: var(--navy); color: var(--paper);
    display: flex; justify-content: space-between; align-items: center; padding: 0 26px;
    border-bottom: 5px solid var(--rule);
  }
  .band__name { font-family: "Cinzel", Georgia, serif; font-size: 19px; line-height: 1.1; }
  .band__title { font-family: "Cinzel", Georgia, serif; font-size: 13px; letter-spacing: .5px; }
  .band__phones { font-size: 12px; line-height: 1.6; }
  .band__phones b { font-weight: 600; display: inline-block; width: 28px; }
  .contact { position: absolute; top: 262px; left: 26px; right: 20px; font-size: 11.5px; color: var(--ink); line-height: 1.75; }
  .contact b { font-weight: 600; }
</style>
</head>
<body>
  <div class="sheet-label" style="left:53px; top:20px;">Front</div>
  <div class="sheet-label" style="left:617px; top:20px;">Back - 1</div>
  <div class="sheet-label" style="left:53px; top:388px;">Back - 2</div>
  <div class="sheet-label" style="left:617px; top:388px;">Back - 3</div>

  <section class="card front" style="left:53px; top:52px;">
    <div class="mark" style="top:32px;"><span class="mark__dot" style="width:18px;height:18px;"></span><span class="mark__name" style="font-size:22px;">TOLLAND</span></div>
    <div class="wordmark" style="top:88px;">
      <div class="wordmark__name">MARCUS TOLLAND</div>
      <div class="wordmark__title">COUNSELLOR AT LAW</div>
    </div>
    <div class="band">
      <div>
        <div class="band__name">MARCUS TOLLAND</div>
        <div class="band__title">COUNSELLOR AT LAW</div>
      </div>
      <div class="band__phones">
        <div><b>tel</b> (555) 014-2280</div>
        <div><b>fax</b> (555) 014-2281</div>
      </div>
    </div>
    <div class="contact">
      <div><b>email</b> mtollandlaw@quillpost.example &nbsp;|&nbsp; <b>web</b> www.tollandlawfirm.example</div>
      <div>482 Brindlecombe Avenue, 3rd Floor Ashgrove, Northvale 08347</div>
    </div>
  </section>

  <section class="card" style="left:617px; top:52px;">
    <div class="mark" style="top:60px;"><span class="mark__dot" style="width:22px;height:22px;"></span><span class="mark__name" style="font-size:26px;">TOLLAND</span></div>
    <div class="wordmark" style="top:130px;">
      <div class="wordmark__name">MARCUS TOLLAND</div>
      <div class="wordmark__title">COUNSELLOR AT LAW</div>
    </div>
    <div class="site" style="top:256px;">WWW.TOLLANDLAWFIRM.EXAMPLE</div>
  </section>

  <section class="card" style="left:53px; top:420px;">
    <div class="mark" style="top:88px;"><span class="mark__dot" style="width:42px;height:42px;border-width:3px;"></span><span class="mark__name" style="font-size:52px;">TOLLAND</span></div>
    <div class="site" style="top:258px;">WWW.TOLLANDLAWFIRM.EXAMPLE</div>
  </section>

  <section class="card card--dark" style="left:617px; top:420px;">
    <div class="mark" style="top:54px;"><span class="mark__dot" style="width:22px;height:22px;"></span><span class="mark__name" style="font-size:26px;">TOLLAND</span></div>
    <div class="wordmark" style="top:124px;">
      <div class="wordmark__name">MARCUS TOLLAND</div>
      <div class="wordmark__title">COUNSELLOR AT LAW</div>
    </div>
    <div class="site" style="top:256px;">WWW.TOLLANDLAWFIRM.EXAMPLE</div>
  </section>
</body>
</html>
```